Pel'k Marrowind Travel

We need a sleek, professional, inviting card to elicit global travel for the experienced and professional traveler. Royal blue, black and silver. (perhaps the wording could be silver with black shadow?-get creative) Maybe a watermark on the front and the full raised logo on the back.
We want a stylish and modern card, but professional.

```html
<!DOCTYPE html>
<html lang="en">
<head>
<meta charset="utf-8">
<title>Pel'k Marrowind Travel – Business Card</title>
<link rel="stylesheet" href="https://fonts.googleapis.com/css2?family=Open+Sans:ital,wght@0,400;0,600;0,700;1,600&display=swap">
<style>
  :root {
    --page: #ececec;
    --black: #000000;
    --royal: #283387;
    --sky: #29a8e0;
    --lime: #8cc63f;
    --silver: #cfd0d2;
    --white: #ffffff;
  }
  * { margin: 0; padding: 0; box-sizing: border-box; }
  html, body { width: 1200px; height: 960px; overflow: hidden; }
  body {
    background: var(--page);
    font-family: "Open Sans", Arial, sans-serif;
    position: relative;
  }
  .card {
    position: absolute;
    left: 295px;
    width: 609px;
    height: 388px;
    overflow: hidden;
    box-shadow: 0 3px 8px rgba(0,0,0,0.25);
  }
  .card--front { top: 77px; background: var(--black); }
  .card--back { top: 507px; background: var(--royal); display: flex; align-items: center; justify-content: center; }

  .card__swoosh { position: absolute; inset: 0; width: 100%; height: 100%; }

  .brand {
    font-weight: 700;
    text-transform: uppercase;
    text-align: center;
    letter-spacing: 0.5px;
  }
  .brand--front {
    position: absolute;
    top: 118px; left: 0; right: 0;
    color: var(--silver);
    font-size: 27px;
    line-height: 1.2;
  }
  .brand--back {
    color: var(--sky);
    font-size: 27px;
    line-height: 1.2;
  }
  .brand__line { display: block; }
  .brand__line--small { font-size: 18px; letter-spacing: 4px; }

  .holder { position: absolute; left: 99px; top: 277px; }
  .holder__name { color: var(--white); font-weight: 700; font-size: 20px; }
  .holder__role { color: var(--lime); font-weight: 600; font-style: italic; font-size: 14px; margin-top: 4px; }

  .contact { position: absolute; left: 352px; top: 282px; list-style: none; color: var(--white); font-size: 13.5px; line-height: 1.45; }
  .contact__item { display: flex; gap: 12px; margin-bottom: 8px; }
  .contact__icon { width: 14px; height: 16px; flex: none; margin-top: 2px; fill: var(--lime); }
</style>
</head>
<body>
  <section class="card card--front">
    <svg class="card__swoosh" viewBox="0 0 609 388" preserveAspectRatio="none" aria-hidden="true">
      <path d="M0,318 Q300,235 490,235 Q570,250 609,285 L609,388 L0,388 Z" fill="var(--royal)"/>
      <path d="M0,288 Q260,222 490,235 Q300,235 0,318 Z" fill="var(--sky)"/>
      <path d="M415,240 Q540,248 609,268 L609,285 Q560,258 415,240 Z" fill="var(--lime)"/>
    </svg>
    <h1 class="brand brand--front">
      <span class="brand__line">Pel'k Marrowind</span>
      <span class="brand__line brand__line--small">Travel</span>
    </h1>
    <div class="holder">
      <p class="holder__name">Maren Tosh Halloway</p>
      <p class="holder__role">Manager</p>
    </div>
    <ul class="contact">
      <li class="contact__item">
        <svg class="contact__icon" viewBox="0 0 24 24"><path d="M6.6 10.8a15.1 15.1 0 0 0 6.6 6.6l2.2-2.2a1 1 0 0 1 1-.25 11.4 11.4 0 0 0 3.6.57 1 1 0 0 1 1 1V20a1 1 0 0 1-1 1A17 17 0 0 1 3 4a1 1 0 0 1 1-1h3.5a1 1 0 0 1 1 1 11.4 11.4 0 0 0 .57 3.6 1 1 0 0 1-.25 1z"/></svg>
        <span>555 018 2240</span>
      </li>
      <li class="contact__item">
        <svg class="contact__icon" viewBox="0 0 24 24"><path d="M12 2a7 7 0 0 0-7 7c0 5.2 7 13 7 13s7-7.8 7-13a7 7 0 0 0-7-7zm0 9.5A2.5 2.5 0 1 1 12 6.5a2.5 2.5 0 0 1 0 5z"/></svg>
        <span>72 Brindle Ave NE, Corvale,<br>GA, 30990</span>
      </li>
    </ul>
  </section>

  <section class="card card--back">
    <h2 class="brand brand--back">
      <span class="brand__line">Pel'k Marrowind</span>
      <span class="brand__line brand__line--small">Travel</span>
    </h2>
  </section>
</body>
</html>
```